BUSINESS CARD DESIGN FOR CONSULTING BUSINESS

I need a business card design containing my logo and slogan for my new consulting business. The consulting business provides the following services: 1) human resource services assistance (payroll, expert advice, developing strategic and recruitment plans and blogs) for small businesses and 2) develops content for small business blogs and online magazines. I plan to expand the business, so I don't want to focus on the services but rather on my initials (HV) for name recognition and the name of the company, Dunmore Advisory Services.
My slogan is Relevant, Innovative, Expert Solutions.
I want a business card that is plain and not busy and contains a logo that reflects my work: consulting and writing. I would also like the business card to include the following contact information in this order: Helena Voss, Principal (lst line) Sr. Consultant (2nd line), 4737 Fenwick Lane, #273614, Sacramento, CA 95818, (3rd line) hvossadvisoryservices@mailpost.example, (4th line), (916) 555-0172 (5th line), (my name, title, business address, email address, and phone number). My business's logo and name, Dunmore Advisory Services, should appear next to each other on the front of the card. The slogan should also be noted on the back of the card. Thanks!

Target Market(s)

Small businesses and governments.

Industry/Entity Type

Human Resources (HR) and Writing, but please focus on consulting services which can be both (HR and writing) or neither.

Logo Text

If possible, please create a abstract logo like the attachment. Or create a logo using my first and last initials (HV) and the word consulting like the Torvald Mesh (TM) example below.

Logo styles of interest
Abstract Logo
Wordmark Logo
Lettermark Logo
Font styles to use
Serif

Colors

Designer to choose colors to be used in the design.

Requirements
Must have
• Please feel free to create your own design as the attachment is just an example to show that I prefer a simple design with that format/layout if possible. The logo should be simple like a lettermark, word mark or abstract logo with the logo on the front and the slogan on the back. Please note my contact information in this order: my name with a title of Principal/Sr. Consultant, my address, email address and my phone number..
Nice to have
• Please see the attached sample design. A blue, or green or blue violet color card may look great. I am also good with simple black and white. Thanks!
Should not have
• Large, busy logo

```html
<!DOCTYPE html>
<html lang="en">
<head>
<meta charset="utf-8">
<title>Dunmore Advisory Services – Business Card</title>
<link rel="stylesheet" href="https://fonts.googleapis.com/css2?family=Montserrat:wght@400;500;600&display=swap">
<style>
  :root {
    --backdrop: #b3b3b3;
    --paper: #ffffff;
    --navy: #034a86;
    --sky: #0f80b0;
    --ink: #111111;
  }
  html, body {
    margin: 0;
    width: 1000px;
    height: 1200px;
    overflow: hidden;
    background: var(--backdrop);
  }
  .sheet {
    position: relative;
    width: 1000px;
    height: 1200px;
  }
  .card {
    position: absolute;
    left: 51px;
    width: 898px;
    height: 539px;
    display: block;
  }
  .card--front { top: 44px; }
  .card--back { top: 625px; }
  .card text { font-family: 'Montserrat', sans-serif; }
  .fill-paper { fill: var(--paper); }
  .fill-navy { fill: var(--navy); }
  .fill-sky { fill: var(--sky); }
  .brand-name { font-weight: 600; letter-spacing: 1px; }
  .brand-sub { font-weight: 600; letter-spacing: 0.5px; }
  .contact { font-size: 26px; fill: var(--ink); font-weight: 400; }
  .contact-name { font-weight: 500; }
  .slogan { font-size: 31px; font-weight: 500; letter-spacing: 1.5px; fill: var(--paper); }
</style>
</head>
<body>
<main class="sheet">

  <!-- Front side -->
  <svg class="card card--front" viewBox="0 0 1062 637" aria-label="Business card front">
    <rect class="fill-paper" width="1062" height="637"/>

    <g class="brand">
      <circle class="fill-navy" cx="560" cy="140" r="56"/>
      <text class="brand-name fill-navy" x="632" y="168" font-size="64">DUNMORE</text>
      <text class="brand-sub fill-sky" x="636" y="192" font-size="22">ADVISORY SERVICES</text>
    </g>

    <g class="contact-block">
      <text class="contact" x="63" y="359"><tspan class="contact-name">Helena Voss</tspan>, Principal</text>
      <text class="contact" x="64" y="389">Sr. Consultant</text>

      <g class="icon icon-pin" transform="translate(64,404)">
        <rect class="fill-navy" width="25" height="25" rx="3"/>
        <circle cx="12.5" cy="10" r="4.5" fill="none" stroke="#fff" stroke-width="2"/>
        <path d="M9 14 L12.5 20 L16 14" fill="none" stroke="#fff" stroke-width="2"/>
      </g>
      <text class="contact" x="101" y="426">4737 Fenwick Lane, #273614, Sacramento, CA 95818</text>

      <g class="icon icon-mail" transform="translate(64,443)">
        <rect class="fill-navy" width="25" height="25" rx="3"/>
        <rect x="5" y="7" width="15" height="11" fill="none" stroke="#fff" stroke-width="1.8"/>
        <path d="M5 7 L12.5 13 L20 7" fill="none" stroke="#fff" stroke-width="1.8"/>
      </g>
      <text class="contact" x="101" y="465">hvossadvisoryservices@mailpost.example</text>

      <g class="icon icon-phone" transform="translate(64,482)">
        <rect class="fill-navy" width="25" height="25" rx="3"/>
        <path d="M8 6 C6 8 7 13 11 17 C14 20 18 20 19 18 L17 15 L14.5 16.5 C12.5 15 10.5 13 9.5 11 L11 8.5 Z" fill="#fff"/>
      </g>
      <text class="contact" x="101" y="504">(916) 555-0172</text>
    </g>

    <g class="waves">
      <path class="fill-sky" d="M0 513 C120 560 240 575 380 555 C560 530 700 470 850 468 C940 468 1010 490 1062 513 L1062 637 L0 637 Z"/>
      <path class="fill-paper" d="M0 548 C120 580 250 592 400 580 C600 560 780 525 900 525 C970 525 1030 540 1062 550 L1062 637 L0 637 Z"/>
      <path class="fill-navy" d="M0 565 C100 590 200 598 320 594 C520 585 720 540 900 538 C970 538 1030 552 1062 565 L1062 637 L0 637 Z"/>
    </g>
  </svg>

  <!-- Back side -->
  <svg class="card card--back" viewBox="0 0 1062 637" aria-label="Business card back">
    <rect class="fill-navy" width="1062" height="637"/>

    <g class="brand">
      <circle class="fill-paper" cx="300" cy="236" r="72"/>
      <text class="brand-name fill-paper" x="395" y="266" font-size="84">DUNMORE</text>
      <text class="brand-sub fill-paper" x="400" y="297" font-size="28">ADVISORY SERVICES</text>
    </g>

    <text class="slogan" x="531" y="440" text-anchor="middle">RELEVANT, INNOVATIVE, EXPERT SOLUTIONS</text>

    <g class="waves">
      <path class="fill-paper" d="M0 513 C120 560 240 575 380 555 C560 530 700 470 850 468 C940 468 1010 490 1062 513 L1062 637 L0 637 Z"/>
      <path class="fill-sky" d="M0 565 C100 590 200 598 320 594 C520 585 720 540 900 538 C970 538 1030 552 1062 565 L1062 637 L0 637 Z"/>
    </g>
  </svg>

</main>
</body>
</html>
```